I will ask the design of the business card

We are looking for business card design of the new company "TORVIK QUANTA WORKS LLC." Based in Azerbaijan.
In case
We are working on Azerbaijan to set up the first exchange of crypto currencies.

The key currency used in exchanges is called "MELDA".
In case
We are doing project to make crypto currency infrastructure.

We provide state-of-the-art technology to the world.

```html
<!DOCTYPE html>
<html lang="en">
<head>
<meta charset="utf-8">
<title>Torvik Quanta Works – Business Card</title>
<link rel="stylesheet" href="https://fonts.googleapis.com/css2?family=Montserrat:wght@300;400;600;700&family=Lato:wght@400;700&display=swap">
<style>
  :root {
    --page: #ededee;
    --card-light: #eeeeee;
    --card-dark: #2a2a2a;
    --card-dark-deep: #242424;
    --accent: #2f7fc8;
    --accent-deep: #2467a8;
    --ink: #5f5f5f;
    --ink-soft: #8a8a8a;
    --white: #ffffff;
    --muted: #cfcfcf;
  }
  * { margin: 0; padding: 0; box-sizing: border-box; }
  html, body { width: 1200px; height: 1153px; overflow: hidden; background: var(--page); }
  body { position: relative; font-family: "Lato", sans-serif; }

  .card {
    position: absolute;
    left: 130px;
    width: 940px;
    height: 520px;
    overflow: hidden;
    box-shadow: 0 10px 30px rgba(0,0,0,0.12);
  }
  .card--front { top: 40px; display: flex; }
  .card--back { top: 595px; background: var(--card-dark); }

  /* Front card */
  .front-brand {
    width: 48%;
    background: var(--card-light);
    display: flex;
    flex-direction: column;
    align-items: center;
    justify-content: center;
    gap: 26px;
  }
  .brand-dot {
    width: 96px; height: 96px; border-radius: 50%;
    background: var(--accent);
  }
  .brand-name {
    font-family: "Montserrat", sans-serif;
    font-weight: 600;
    color: var(--ink);
    font-size: 34px;
    letter-spacing: 1px;
    text-align: center;
    line-height: 1.25;
  }

  .front-contact {
    width: 52%;
    background: var(--card-dark);
    padding: 70px 60px 0 56px;
    color: var(--white);
    position: relative;
  }
  .front-contact .map-texture {
    position: absolute; inset: 0;
    background: radial-gradient(ellipse at 60% 60%, #333 0%, var(--card-dark) 70%);
  }
  .contact-inner { position: relative; }
  .person-name {
    font-family: "Montserrat", sans-serif;
    font-size: 31px;
    letter-spacing: 2px;
  }
  .person-name .first { font-weight: 700; }
  .person-name .last { font-weight: 300; }
  .person-role {
    font-family: "Montserrat", sans-serif;
    font-size: 16px;
    letter-spacing: 2.5px;
    margin-top: 4px;
    color: var(--muted);
  }
  .rule { height: 2px; background: var(--accent); margin: 22px 0 34px; width: 100%; }
  .contact-list { list-style: none; display: flex; flex-direction: column; gap: 22px; }
  .contact-row { display: flex; align-items: flex-start; gap: 20px; font-size: 19px; line-height: 1.3; }
  .contact-icon {
    flex: 0 0 40px; width: 40px; height: 40px; border-radius: 7px;
    background: linear-gradient(var(--accent), var(--accent-deep));
    display: flex; align-items: center; justify-content: center;
  }

  /* Back card */
  .network-texture {
    position: absolute; inset: 0;
    background: radial-gradient(ellipse at 50% 45%, #303030 0%, var(--card-dark-deep) 80%);
  }
  .back-content {
    position: absolute; inset: 0;
    display: flex; flex-direction: column; align-items: center; justify-content: center;
    color: var(--white);
  }
  .back-dot { width: 70px; height: 70px; border-radius: 50%; background: var(--white); margin-bottom: 22px; }
  .coin-name {
    font-family: "Montserrat", sans-serif;
    font-weight: 300;
    font-size: 64px;
    letter-spacing: 6px;
  }
  .tagline {
    font-family: "Montserrat", sans-serif;
    font-weight: 400;
    font-size: 19px;
    letter-spacing: 1.5px;
    text-align: center;
    margin-top: 18px;
    line-height: 1.45;
  }
</style>
</head>
<body>

<section class="card card--front">
  <div class="front-brand">
    <div class="brand-dot"></div>
    <p class="brand-name">TORVIK QUANTA<br>WORKS LLC.</p>
  </div>
  <div class="front-contact">
    <div class="map-texture" role="img" aria-label="Faint world map texture"></div>
    <div class="contact-inner">
      <h1 class="person-name"><span class="first">ELNUR</span> <span class="last">KAZIMOV</span></h1>
      <p class="person-role">MANAGING DIRECTOR</p>
      <div class="rule"></div>
      <ul class="contact-list">
        <li class="contact-row">
          <span class="contact-icon">
            <svg width="20" height="20" viewBox="0 0 24 24"><path fill="#fff" d="M6.6 10.8a15.1 15.1 0 0 0 6.6 6.6l2.2-2.2a1 1 0 0 1 1-.25 11.4 11.4 0 0 0 3.6.57 1 1 0 0 1 1 1V20a1 1 0 0 1-1 1A17 17 0 0 1 3 4a1 1 0 0 1 1-1h3.5a1 1 0 0 1 1 1c0 1.25.2 2.45.57 3.57a1 1 0 0 1-.25 1z"/></svg>
          </span>
          <span>+1 555 014 2020<br>+1 555 014 2020</span>
        </li>
        <li class="contact-row">
          <span class="contact-icon">
            <svg width="20" height="20" viewBox="0 0 24 24" fill="none" stroke="#fff" stroke-width="2"><circle cx="12" cy="12" r="9"/><path d="M3 12h18M12 3c3 3 3 15 0 18M12 3c-3 3-3 15 0 18"/></svg>
          </span>
          <span>hello@torvikquanta.net<br>www.torvikquanta.net</span>
        </li>
        <li class="contact-row">
          <span class="contact-icon">
            <svg width="20" height="20" viewBox="0 0 24 24"><path fill="#fff" d="M12 3 2 12h3v8h5v-5h4v5h5v-8h3z"/></svg>
          </span>
          <span>AZ1010, 8/3N, Nizami Str.<br>Baku City, Azerbaijan</span>
        </li>
      </ul>
    </div>
  </div>
</section>

<section class="card card--back">
  <div class="network-texture" role="img" aria-label="Subtle connected-node network pattern"></div>
  <div class="back-content">
    <div class="back-dot"></div>
    <p class="coin-name">MELDA</p>
    <p class="tagline">Decentralized value exchange platform<br>for Real Business Market</p>
  </div>
</section>

</body>
</html>
```